HTML Email marketing template for supplement campaign

I want a general template for email marketing in HTML format. I have a product line of supplements that I want to trade out for email marketing campaigns. I will need to use a bottle renderings, hyper links to product landing pages, and campaign literature/call to action. Coupon codes, QR code to product landing page

Target Market(s)

Elderly 50+

Industry/Entity Type

All Natural Supplement pain relief

Colors

Designer to choose colors to be used in the design.

Requirements
Must have
• All-natural formula: Our pain and inflammation relief supplement is made from carefully selected natural ingredients, providing you with a holistic and gentle approach to relieving pain and inflammation. - Powerful anti-inflammatory properties: Packed with potent botanical extracts and natural compounds, our supplement helps reduce inflammation and soothe discomfort, promoting overall well-being. - No harsh chemicals or artificial additives: We believe in providing you with a pure and clean product. Our supplement is free from harsh chemicals, artificial additives, and fillers, ensuring a natural and safe experience. - Enhanced absorption: Our formula is designed to maximize absorption and bioavailability, allowing your body to efficiently utilize the beneficial properties of the ingredients for optimal results. - Supports overall well-being: In addition to pain and inflammation relief, our supplement promotes overall well-being by supporting a healthy inflammatory response, joint health, and a balanced immune system. Higher Quality and more potent than Ember Quell (TM)
Nice to have
• black and gold theme

```html
<!DOCTYPE html>
<html lang="en">
<head>
<meta charset="UTF-8">
<title>Aurevia – All-Natural Pain and Inflammation Relief</title>
<link href="https://fonts.googleapis.com/css2?family=Open+Sans:wght@400;600;700&display=swap" rel="stylesheet">
<style>
  :root {
    --black: #000000;
    --white: #ffffff;
    --gold: #d4af25;
    --brand-gold: #c9a063;
    --yellow: #f5ec00;
    --body-grey: #555555;
    --ink: #111111;
  }
  * { box-sizing: border-box; margin: 0; padding: 0; }
  html, body { width: 1200px; height: 3027px; overflow: hidden; }
  body {
    font-family: "Open Sans", Arial, sans-serif;
    background: var(--white);
    position: relative;
  }
  .hero {
    position: absolute; left: 0; top: 0; width: 1200px; height: 595px;
    background: var(--black); color: var(--white); text-align: center;
  }
  .brand-name {
    position: absolute; left: 0; width: 100%;
    color: var(--brand-gold); font-weight: 400; letter-spacing: 10px;
  }
  .hero .brand-name { top: 120px; font-size: 54px; line-height: 60px; }
  .hero-title {
    position: absolute; top: 270px; left: 0; width: 100%;
    font-size: 41px; line-height: 45px; font-weight: 400;
  }
  .hero-title strong { color: var(--yellow); font-weight: 700; }
  .hero-rule {
    position: absolute; top: 434px; left: 400px; width: 400px; height: 1px;
    background: var(--white);
  }
  .formula-title {
    position: absolute; top: 466px; left: 0; width: 100%;
    color: var(--yellow); font-weight: 700; font-size: 22px; line-height: 28px;
  }
  .formula-text {
    position: absolute; top: 493px; left: 190px; width: 820px;
    font-size: 21.5px; line-height: 26px;
  }
  .bottle {
    position: absolute; left: 170px; top: 617px; width: 247px; height: 376px;
    border-radius: 28px 28px 34px 34px;
    background: linear-gradient(90deg, #111 0%, #2a2a2a 40%, #0b0b0b 100%);
    box-shadow: 0 6px 14px rgba(0,0,0,0.35);
  }
  .btn {
    position: absolute; display: flex; align-items: center; justify-content: center;
    background: var(--gold); color: var(--white); text-decoration: none;
    border-radius: 4px; font-size: 25px;
  }
  .btn-buy { left: 175px; top: 1033px; width: 234px; height: 63px; }
  .benefits {
    position: absolute; left: 491px; top: 616px; width: 560px;
    color: var(--ink); font-size: 22.5px; line-height: 26.7px; list-style: none;
  }
  .benefits li { position: relative; }
  .benefits li::before {
    content: ""; position: absolute; left: -19px; top: 11px;
    width: 7px; height: 7px; border-radius: 50%; background: var(--ink);
  }
  .pitch-title {
    position: absolute; top: 1180px; left: 200px; width: 800px; text-align: center;
    color: var(--gold); font-size: 48px; line-height: 55px; font-weight: 400;
  }
  .pitch {
    position: absolute; top: 1380px; left: 155px; width: 887px;
    color: var(--body-grey); font-size: 22.5px; line-height: 33px; text-align: justify;
  }
  .pitch p { margin-bottom: 33px; }
  .pitch .closing { color: var(--body-grey); font-weight: 700; }
  .pitch .closing span { color: var(--gold); }
  .btn-browse { left: 155px; top: 2236px; width: 293px; height: 64px; }
  .footer {
    position: absolute; left: 0; top: 2356px; width: 1200px; height: 671px;
    background: var(--black); color: var(--white); text-align: center;
  }
  .footer .brand-name { top: 80px; font-size: 44px; line-height: 52px; }
  .site-url {
    position: absolute; top: 185px; left: 0; width: 100%;
    font-size: 40px; line-height: 48px; color: var(--white); text-decoration: none;
  }
  .footer-rule {
    position: absolute; left: 155px; width: 887px; height: 1px; background: var(--white);
  }
  .notice {
    position: absolute; top: 306px; left: 0; width: 100%;
    font-size: 22px; line-height: 26px;
  }
  .footer-links a {
    position: absolute; top: 424px; width: 300px; margin-left: -150px;
    color: var(--white); text-decoration: none; font-size: 22px; line-height: 30px;
  }
  .footer-links .underlined { text-decoration: underline; }
  .copyright {
    position: absolute; top: 511px; left: 0; width: 100%; font-size: 18.5px; line-height: 26px;
  }
</style>
</head>
<body>
  <header class="hero">
    <div class="brand-name">Aurevia</div>
    <h1 class="hero-title">Introducing our<br><strong>all-natural pain</strong> and <strong>inflammation relief</strong><br>product!</h1>
    <div class="hero-rule"></div>
    <div class="formula-title">All-natural formula</div>
    <p class="formula-text">Our pain and inflammation relief supplement is made from carefully selected natural ingredients, providing you with a holistic and gentle approach to relieving pain and inflammation.</p>
  </header>

  <div class="bottle" role="img" aria-label="Black supplement tub labelled Calmora, pain and inflammation support"></div>
  <a class="btn btn-buy" href="#">Buy Product</a>

  <ul class="benefits">
    <li>Powerful anti-inflammatory properties: Packed with potent botanical extracts and natural compounds, our supplement helps reduce inflammation and soothe discomfort, promoting overall well-being.</li>
    <li>No harsh chemicals or artificial additives: We believe in providing you with a pure and clean product. Our supplement is free from harsh chemicals, artificial additives, and fillers, ensuring a natural and safe experience.</li>
    <li>Enhanced absorption: Our formula is designed to maximize absorption and bioavailability, allowing your body to efficiently utilize the beneficial properties of the ingredients for optimal results.</li>
    <li>Supports overall well-being: In addition to pain and inflammation relief, our supplement promotes overall well-being by supporting a healthy inflammatory response, joint health, and a balanced immune system.</li>
  </ul>

  <h2 class="pitch-title">Are you tired of relying on synthetic medications to manage your pain and inflammation?</h2>

  <section class="pitch">
    <p>Look no further, because we have the perfect solution for you. Our all-natural pain and inflammation relief formula is carefully crafted using only the finest natural ingredients, specifically chosen for their powerful healing properties.</p>
    <p>Say goodbye to discomfort and hello to relief with our product. Designed to target pain and inflammation at its source, our formula works harmoniously with your body's natural processes to provide effective and long-lasting relief.</p>
    <p>We understand the importance of using natural ingredients, which is why we have carefully selected a blend of botanical extracts and essential fish oils known for their anti-inflammatory and analgesic properties. These ingredients work together synergistically to reduce swelling, soothe sore muscles, and alleviate pain without any harsh side effects.</p>
    <p>Our product is not only effective but also safe to use. Free from artificial additives, preservatives, and synthetic chemicals, you can trust that you are giving your body the best care possible.</p>
    <p>Whether you suffer from chronic pain, sports injuries, arthritis, or general inflammation, our all-natural pain and inflammation relief product is here to help. Experience the power of nature and regain control over your well-being.</p>
    <p class="closing">Don't let pain hold you back any longer.<br><span>Try our all-natural pain and inflammation relief product today and discover the natural path to a pain-free life</span>.</p>
  </section>
  <a class="btn btn-browse" href="#">BROWSE PRODUCTS</a>

  <footer class="footer">
    <div class="brand-name">Aurevia</div>
    <a class="site-url" href="#">https://aureviawellness.com</a>
    <div class="footer-rule" style="top:277px"></div>
    <p class="notice">You are receiving this email because you visited our site<br>or asked us about the regular newsletter</p>
    <div class="footer-rule" style="top:393px"></div>
    <nav class="footer-links">
      <a href="#" style="left:291px">Terms and Service</a>
      <a href="#" class="underlined" style="left:596px">Privacy Policy</a>
      <a href="#" style="left:904px">Unsubscribe</a>
    </nav>
    <p class="copyright">© 2024 Aurevia Wellness All Rights Reserved.</p>
  </footer>
</body>
</html>
```